Product sheet for managing talented people!

We need a new product sheet to describe our method of helping organisations to manage their talented people! We have selected a rowing team as the graphical theme (sample attached - please select or suggest a new picture if you want). We have also attached a powerpoint slide with our model (this is the service we offer).

FRONT PAGE

We are looking for an eye-catching front page that uses our 1. "Kestrel Skills Model"; 2. a picture of a rowing team of 8, and 3. our logo and 1800 KESTRL phone number (1800 537 875).

Step 1 - Assess key positions to determine your Talent Management Priorities.

Step 2 - Organisational psychology support helps individuals self-evaluate (see page 2 for details).

Step 3 - Facilitate agreement with manager and embed best-practice in organisational fairness.

Step 4 - Tailor career development and redeployment options based on shared understanding.

Step 5 - Evaluate ROI for individual performance and engagement.

BACK PAGE

The second page will have more detail of each of the talent categories also included in the powerpoint slide. Logo attached also. Please also view our website as the graphics should give you a sense of the look and feel of our brand - www.kestrelsm.com.au We have also added another flyer that we still use - please do not reverse the logo on this project - use in current form. CORPORATE LOGO / COLOUR GUIDE
C100 M50 Y0 K0
C100 M50 Y0 K0
C100 M50 Y0 K0
Gradient
C100 M60 Y0 K40
C100 M45 Y0 K0
C100 M20 Y0 K0
C70 M0 Y0 K0
PMS 2935 C
PMS 2935 C 75% Tint
PMS 2935 C
PMS Process Cyan C

The successful flyer will need to be print ready (as per attached example) and in pdf form so that we can print and/or send as a PDF.

Thanks.

Target Market(s)

Human Resource Managers in business and government.

Industry/Entity Type

Product

Requirements
Must have
• Eye-catching graphics with a rowing team theme. Colours consistent with our corporate colour codes.
Nice to have
• Please add small "trademark" symbol to the logo. This is small TM in a circle and usually placed at top right hand of logo. PLease add our website address www.kestrelsm.com
Should not have
• Please do not "reverse" the logo - use as is.

```html
<!DOCTYPE html>
<html lang="en">
<head>
<meta charset="utf-8">
<title>Kestrel Skills Model – Product Sheet</title>
<link rel="stylesheet" href="https://fonts.googleapis.com/css2?family=Tinos:wght@400;700&family=Lato:ital,wght@1,700&family=Roboto+Condensed:wght@700&family=Montserrat:wght@500&display=swap">
<style>
  :root {
    --brand-blue: #3d4fa3;
    --brand-blue-dark: #2f3f8c;
    --ink: #262626;
    --charcoal: #2d2d2d;
    --paper: #ffffff;
    --backdrop: #e8e5e1;
    --muted: #5a5a5a;
  }
  * { margin: 0; padding: 0; box-sizing: border-box; }
  html, body {
    width: 907px; height: 1200px; overflow: hidden;
    background: var(--backdrop);
  }
  .sheet {
    position: absolute; left: 75px; top: 68px;
    width: 755px; height: 1060px;
    background: var(--paper);
    overflow: hidden;
    box-shadow: 0 2px 8px rgba(0,0,0,0.15);
  }
  .sheet-art { position: absolute; inset: 0; width: 755px; height: 1060px; }

  .brand {
    position: absolute; left: 556px; top: 30px; width: 182px;
    text-align: center; color: var(--brand-blue);
    font-family: "Tinos", "Times New Roman", serif; font-weight: 400;
  }
  .brand-mark {
    display: block; width: 22px; height: 22px; margin: 0 auto 8px;
    background: var(--brand-blue);
  }
  .brand-name { display: block; font-size: 38px; line-height: 1; letter-spacing: 0.5px; }
  .brand-tagline { display: block; font-size: 10px; letter-spacing: 1.4px; margin-top: 4px; }

  .headline {
    position: absolute; left: 22px; top: 572px;
    font-family: "Tinos", "Times New Roman", serif;
  }
  .headline-brand { display: block; color: var(--brand-blue); font-size: 62px; font-weight: 400; line-height: 1; letter-spacing: 1px; }
  .headline-model { display: block; color: var(--ink); font-size: 50px; font-weight: 700; line-height: 1.1; }

  .step {
    position: absolute; width: 342px; height: 62px;
  }
  .step-pill {
    position: absolute; left: 28px; top: 10px; right: 0; height: 44px;
    border: 2.5px solid var(--brand-blue); border-radius: 22px;
    background: var(--paper);
    padding: 6px 14px 0 42px;
    font-family: "Lato", Arial, sans-serif; font-style: italic; font-weight: 700;
    font-size: 10.5px; line-height: 1.25; color: var(--ink);
  }
  .step-pill--three-line { padding-top: 3px; line-height: 1.2; }
  .step-badge {
    position: absolute; left: 0; top: 0; width: 64px; height: 64px;
    border-radius: 50%; background: var(--brand-blue);
    border: 3px solid var(--paper); box-shadow: 0 0 0 2px var(--brand-blue);
    color: var(--paper);
    display: flex; align-items: center; justify-content: center;
  }
  .step-label {
    font-family: "Lato", Arial, sans-serif; font-style: normal; font-size: 9px; font-weight: 700;
    transform: rotate(-90deg); letter-spacing: 1px; margin-right: -6px;
  }
  .step-number {
    font-family: "Tinos", "Times New Roman", serif; font-size: 36px; font-weight: 400;
  }
  .step--1 { left: 21px; top: 708px; }
  .step--2 { left: 403px; top: 708px; width: 320px; }
  .step--3 { left: 21px; top: 788px; }
  .step--4 { left: 403px; top: 788px; width: 320px; }
  .step--5 { left: 21px; top: 868px; width: 336px; }

  .hotline {
    position: absolute; left: 416px; top: 880px;
    display: flex; align-items: center; gap: 12px;
  }
  .hotline-number {
    font-family: "Roboto Condensed", Arial, sans-serif; font-weight: 700;
    font-size: 40px; color: var(--brand-blue); letter-spacing: 0.5px;
  }

  .website {
    position: absolute; left: 0; right: 0; top: 1030px;
    text-align: center; color: var(--paper);
    font-family: "Montserrat", Arial, sans-serif; font-weight: 500;
    font-size: 13px; letter-spacing: 5px;
  }
</style>
</head>
<body>
<main class="sheet">
  <svg class="sheet-art" viewBox="0 0 755 1060">
    <defs>
      <linearGradient id="heroTone" x1="0" y1="0" x2="1" y2="1">
        <stop offset="0" stop-color="#6f8a5c"/>
        <stop offset="0.35" stop-color="#c9ccd0"/>
        <stop offset="0.7" stop-color="#8d95a8"/>
        <stop offset="1" stop-color="#3b3f52"/>
      </linearGradient>
      <linearGradient id="fadedTone" x1="0" y1="0" x2="0" y2="1">
        <stop offset="0" stop-color="#e9e9e9"/>
        <stop offset="0.5" stop-color="#f4f4f4"/>
        <stop offset="1" stop-color="#d9d9d9"/>
      </linearGradient>
      <radialGradient id="waterTone" cx="0.5" cy="0.5" r="0.6">
        <stop offset="0" stop-color="#5d7a72"/>
        <stop offset="1" stop-color="#3f5650"/>
      </radialGradient>
      <radialGradient id="greenWaterTone" cx="0.5" cy="0.5" r="0.6">
        <stop offset="0" stop-color="#6e9a4c"/>
        <stop offset="1" stop-color="#4d7a36"/>
      </radialGradient>
    </defs>

    <rect class="backdrop-photo" x="0" y="470" width="755" height="480" fill="url(#fadedTone)"
          role="img" aria-label="Faded greyscale photo of rowers at the oars"/>

    <path class="hero-photo" d="M0 0 H370 C450 70 530 170 620 270 C690 345 730 390 755 440 C500 425 220 470 0 530 Z"
          fill="url(#heroTone)" role="img" aria-label="Photo of a women's rowing crew pulling oars in unison"/>
    <path d="M370 0 C450 70 530 170 620 270 C690 345 730 390 755 440" fill="none" stroke="var(--charcoal)" stroke-width="5"/>
    <path d="M388 0 C468 68 548 166 636 262 C704 336 744 380 770 430" fill="none" stroke="var(--brand-blue)" stroke-width="5"/>

    <path d="M0 530 C220 470 500 425 755 440 V462 C500 452 220 500 0 575 Z" fill="var(--brand-blue)"/>
    <path d="M0 580 C220 505 500 458 755 468" fill="none" stroke="var(--charcoal)" stroke-width="3"/>

    <circle cx="357" cy="474" r="120" fill="var(--charcoal)"/>
    <circle cx="357" cy="474" r="108" fill="var(--brand-blue)"/>
    <circle cx="357" cy="474" r="102" fill="url(#waterTone)" role="img" aria-label="Photo of a men's rowing eight seen from the bow"/>

    <circle cx="620" cy="500" r="122" fill="var(--charcoal)"/>
    <circle cx="620" cy="500" r="110" fill="var(--brand-blue)"/>
    <circle cx="620" cy="500" r="104" fill="url(#greenWaterTone)" role="img" aria-label="Aerial photo of a rowing eight on green water"/>

    <path d="M0 915 Q377 985 755 915" fill="none" stroke="var(--brand-blue)" stroke-width="4"/>
    <path d="M0 928 Q377 1000 755 928 V1060 H0 Z" fill="var(--charcoal)"/>
  </svg>

  <div class="brand">
    <span class="brand-mark"></span>
    <span class="brand-name">KESTREL</span>
    <span class="brand-tagline">SKILLS MANAGEMENT</span>
  </div>

  <h1 class="headline">
    <span class="headline-brand">KESTREL</span>
    <span class="headline-model">Skills Model</span>
  </h1>

  <div class="step step--1">
    <p class="step-pill">Assess key positions to determine your<br>Talent Management Priorities.</p>
    <div class="step-badge"><span class="step-label">STEP</span><span class="step-number">1</span></div>
  </div>
  <div class="step step--2">
    <p class="step-pill">Organisational psychology support helps<br>individuals self-evaluate</p>
    <div class="step-badge"><span class="step-label">STEP</span><span class="step-number">2</span></div>
  </div>
  <div class="step step--3">
    <p class="step-pill">Facilitate agreement with manager and embed<br>best-practice in organisational fairness.</p>
    <div class="step-badge"><span class="step-label">STEP</span><span class="step-number">3</span></div>
  </div>
  <div class="step step--4">
    <p class="step-pill step-pill--three-line">Step 4 - Tailor career development and<br>redeployment options based on shared<br>understanding.</p>
    <div class="step-badge"><span class="step-label">STEP</span><span class="step-number">4</span></div>
  </div>
  <div class="step step--5">
    <p class="step-pill">Evaluate ROI for individual<br>performance and engagement.</p>
    <div class="step-badge"><span class="step-label">STEP</span><span class="step-number">5</span></div>
  </div>

  <div class="hotline">
    <svg width="30" height="46" viewBox="0 0 30 46" role="img" aria-label="Phone">
      <rect x="2" y="2" width="26" height="42" rx="4" fill="var(--charcoal)"/>
      <rect x="6" y="7" width="18" height="13" fill="#ffffff"/>
      <g fill="#ffffff">
        <rect x="6" y="24" width="4" height="3"/><rect x="13" y="24" width="4" height="3"/><rect x="20" y="24" width="4" height="3"/>
        <rect x="6" y="30" width="4" height="3"/><rect x="13" y="30" width="4" height="3"/><rect x="20" y="30" width="4" height="3"/>
        <rect x="6" y="36" width="4" height="3"/><rect x="13" y="36" width="4" height="3"/><rect x="20" y="36" width="4" height="3"/>
      </g>
    </svg>
    <span class="hotline-number">1800 537 875</span>
  </div>

  <p class="website">www.kestrelsm.com</p>
</main>
</body>
</html>
```